Consulting company business cards

We have a base design, but would be willing to update. We have a new logo/"tag" that needs to be added. Current business card design is attached for reference into our "style."

Industry/Entity Type

Business

Contact Information for Business Card

Should contain name and title, office number, mobile number if appropriate, e-mail, website, physical address, and company logo.

Font styles to use
Other font styles liked:
• See current card design on DrovankBCard

Colors
0455a3
85acd3
aaaaaa

Requirements
Must have
• Our colors are navy blue, gray, and a lighter blue
Nice to have
• Design that I can easily drop in new names/titles as we hire employees.

```html
<!DOCTYPE html>
<html lang="en">
<head>
<meta charset="utf-8">
<title>Harrowby Business Cards</title>
<link rel="stylesheet" href="https://fonts.googleapis.com/css2?family=Montserrat:wght@400;500;600;700&family=Oswald:wght@700&display=swap">
<style>
  :root {
    --navy: #04314f;
    --sky: #3bb5e6;
    --pale-blue: #85acd3;
    --grey: #aaaaaa;
    --ink: #1f3a52;
    --paper: #ffffff;
    --stage: #e6e8eb;
  }
  * { margin: 0; padding: 0; box-sizing: border-box; }
  html, body {
    width: 1200px; height: 900px; overflow: hidden;
    background: var(--stage);
    font-family: "Montserrat", Arial, sans-serif;
  }
  .sheet { position: relative; width: 1200px; height: 900px; }
  .card {
    position: absolute; left: 285px; width: 630px; height: 360px;
    border-radius: 22px; overflow: hidden;
  }
  .card-front { top: 60px; background: var(--sky); }
  .card-back { top: 480px; background: var(--paper); }

  .mascot-area {
    position: absolute; left: 250px; top: 90px; width: 135px; height: 150px;
    border-radius: 50% 45% 40% 50%;
    background: radial-gradient(circle at 45% 40%, #0b3f62, var(--navy));
  }
  .front-web {
    position: absolute; left: 28px; bottom: 26px;
    color: var(--paper); font-size: 17px; letter-spacing: 0.5px;
  }
  .front-web strong { font-weight: 700; }

  .brand {
    position: absolute; left: 40px; top: 112px; width: 280px;
  }
  .brand-row { display: flex; align-items: center; gap: 10px; }
  .brand-name {
    font-family: "Oswald", Impact, sans-serif; font-weight: 700;
    font-size: 44px; line-height: 1; color: var(--navy); letter-spacing: 1px;
  }
  .brand-dot {
    width: 34px; height: 34px; border-radius: 50%; background: var(--pale-blue); flex: none;
  }
  .brand-tag {
    margin-top: 8px; font-size: 11px; letter-spacing: 1.3px;
    color: var(--grey); text-transform: uppercase; white-space: nowrap;
  }

  .contact {
    position: absolute; left: 360px; top: 70px; color: var(--ink);
  }
  .person-name {
    font-size: 21px; font-weight: 700; color: var(--sky);
    letter-spacing: 1px; text-transform: uppercase; white-space: nowrap;
  }
  .person-title {
    font-size: 14px; letter-spacing: 0.8px; text-transform: uppercase;
    margin-top: 2px;
  }
  .address { margin-top: 16px; font-size: 14px; line-height: 1.4; }
  .lines { margin-top: 14px; list-style: none; font-size: 14px; }
  .lines li { display: flex; align-items: center; gap: 9px; line-height: 1.55; white-space: nowrap; }
  .lines svg { width: 12px; height: 12px; fill: var(--sky); flex: none; }
  .lines strong { color: var(--sky); font-weight: 600; }
</style>
</head>
<body>
<main class="sheet">
  <section class="card card-front">
    <div class="mascot-area" role="img" aria-label="Illustration of a dog's head in profile"></div>
    <p class="front-web">www.<strong>HARROWBYTECH</strong>.com</p>
  </section>

  <section class="card card-back">
    <div class="brand">
      <div class="brand-row">
        <span class="brand-name">HARROWBY</span>
        <span class="brand-dot"></span>
      </div>
      <p class="brand-tag">A Cloud Consulting Company</p>
    </div>

    <div class="contact">
      <h1 class="person-name">Marissa Drovank</h1>
      <p class="person-title">Office Manager</p>
      <p class="address">1187 w 54th st<br>carmel indiana 46032</p>
      <ul class="lines">
        <li><svg viewBox="0 0 12 12"><path d="M2.5 0.5 L4.5 0.5 L5.3 3 L4 4.2 Q5.2 6.8 7.8 8 L9 6.7 L11.5 7.5 L11.5 9.5 Q11.5 11.5 9.5 11.5 Q0.5 10.5 0.5 2.5 Q0.5 0.5 2.5 0.5Z"/></svg><span>317 555 0148</span></li>
        <li><svg viewBox="0 0 12 12"><rect x="3" y="0.5" width="6" height="11" rx="1.2"/></svg><span>317 555 0193</span></li>
        <li><svg viewBox="0 0 12 12"><path d="M0.5 2 H11.5 V10 H0.5Z M1.5 3 L6 6.5 L10.5 3" fill="none" stroke="#3bb5e6" stroke-width="1.2"/></svg><span>mdrovank@harrowbytech.com</span></li>
        <li><svg viewBox="0 0 12 12"><circle cx="6" cy="6" r="5.3" fill="none" stroke="#3bb5e6" stroke-width="1.2"/><path d="M0.7 6 H11.3 M6 0.7 Q3 6 6 11.3 M6 0.7 Q9 6 6 11.3" fill="none" stroke="#3bb5e6" stroke-width="1"/></svg><span>www.<strong>HARROWBYTECH</strong>.com</span></li>
      </ul>
    </div>
  </section>
</main>
</body>
</html>
```